Can you make FairlyNeat look better than average? We need business cards and a logo refresh :-)

REVISED BRIEF

PRIORITY

VECTOR LOGO

Create a vector version of our existing logo. The logo must not change from its current design, weight or font.

Deliverables

- Logo in blue (#2540BB)
- Logo in white (#FFFFFF)
- Logo in grey (#36454F)
- All logos on transparent background
- All logos in PNG & SVG formats. (SVG must NOT distort stroke width when resized)

BRAND MARK

Create a brand mark for use with the logo. This should be possible to used with the logo and on its own as a stand alone graphical device that represents the FAIRLYNEAT brand.

https://quellbrik.com/resources/glossary/what-is-a-brand-mark

Deliverables

- Brand Mark in blue (#2540BB)
- Brand Mark in white (#FFFFFF)
- Brand Mark in grey (#36454F)
- Brand Mark on transparent background
- Brand Mark in PNG & SVG formats. (SVG must NOT distort stroke width when resized)
- Logo combined with Brand Mark (colours and formats)
.

Business Card Layout

Create 2 layouts with the following details:-

Marcus Delaney
Co-Founder & Chief Product Officer

marcus@fairlyneat.nz
www.fairlyneat.nz
0279831465

Callum Ferris
Founder & CEO

hello@fairlyneat.nz
www.fairlyneat.nz
021 684 2590

DESIGN CONSIDERATIONS

Create versions with ‘Shaping Causes With Heart’ tag line incorporated within the design and without (maintain separation of logo from tag line)

- Create a version with and without the brand mark
- Keep it clean and simple but elevate the design with subtle design effects
- Consider use of raised spot gloss colour (this can be white on white for subtle or blue on blue or blue on white)
- Consider use of spot gloss colour (this can be white on white for subtle or blue on blue or blue on white)
- Consider use of letterpress indentation
- Ensure contact details are legible, use sans-serif font

PREVIOUS BRIEF

We need a business card design for our business FairlyNeat. We are a purpose driven brand and media agency that helps brands and charities plan and buy traditional media campaigns (TV, Radio, Print, Outdoor etc). We give a significant amount of the media booking fees we receive from media vendors to charity in the name of our clients. https://www.plinkwork.com/posts/wearefairlyneat_giveback-fairlyneat-shapingcauseswithheart-activity-5829170364418205731-Rtqe

Our strapline is 'Shaping Causes With Heart'.

We want to keep our logo design as it is but it does need tightening up and made into a proper vector image as it's been created from a font.

Our brand colour is #2540BB and we need to keep this.

Our brand is professional but human, warm and engaging and doesn't take itself too seriously.

Things We Need
- vectorisation and tidying up of existing logo
- We'd like you to think about how we can incorporate a brand mark with the logo to add another dimension to our brand
- business card layout and design
- we'll be using zentiprint.com to print the cards so please take a look at the options they have (spot gloss, foil, letterpress, square cards and even the backs of the cards can have a different design on every single card!
- potential opportunity for different famous quotes on the back or imagery or slight design differences
- we'd be open to the use of an emoji or emojiis as the brandmark or to be incorporated into the card designs
- we can have as many different design batches as we like for the backs of the cards

https://www.zentiprint.com/au/business-cards

We want to make an impact, we want to be seen as professional but fun, we want to be different.

Here's a press release of what we're about.

https://adwirely.co.nz/movings-shakings/fairlyneat-welcomes-marcus-delaney-as-co-founder/

Be bold, be different, there is no such thing as a bad idea. We're open to anything so please bring your best ideas and have fun with it! Go crazy if you like!
____________
Marcus Delaney
marcus@fairlyneat.nz
0279831465

Callum Ferris
Founder & CEO
hello@fairlyneat.nz
021 684 2590

Shaping Causes With Heart

________

These are the only details we MUST have on the cards, the rest is up to you. Just make sure you use all of your creativity but don't feel the need to crowd the card with too much, let it breathe as well.

In terms of font for the details, we'll leave that up to you, just ensure it's legible. Oh and please don't take any design inspiration from our website - that will be changing!

Please don't let the design and layout look cheap and tacky though. It needs to still feel premium but personable.

Thanks

Marcus

Many designs are changing the logo and this was NOT in the brief. We need a brand mark to complement the logo. We need to see the logo with and without the brand mark. We need to see the business card with both logo + brand mark and logo on its own We need to see the business card with and without the tagline 'Shaping Causes With Heart'

purpose driven Brand & Media Agency

Shaping Causes With Heart
Marcus Delaney, Co-Founder & Chief Product Officer, marcus@fairlyneat.nz fairlyneet.nz, 0279 831 465

Callum Ferris, Founder & CEO hello@fairlyneat.nz, fairlyneet.nz, 021 684 2590

Serif
Sans Serif

0054AA
0677BA
7BADD7
CADEEF
E8F1F8

• brand mark, vector version of existing logo, Shaping Causes With Heart tagline, existing logo traced and vectorised. Must fully explore the design options from zentiprint.com that can enhance the overall card design
• brandmark to help elevate the logo, maybe incorporate some other design elements into the card like lines, or grids.
• A cheap look and feel

```html
<!DOCTYPE html>
<html lang="en">
<head>
<meta charset="utf-8">
<title>FairlyNeat Business Cards</title>
<link rel="stylesheet" href="https://fonts.googleapis.com/css2?family=Poppins:wght@400;500;600&display=swap">
<style>
  :root {
    --brand-blue: #3a4fa6;
    --card-white: #ffffff;
    --backdrop: #e8e4de;
    --shadow: rgba(40, 30, 20, 0.25);
  }
  * { box-sizing: border-box; margin: 0; padding: 0; }
  html, body {
    width: 1189px;
    height: 1200px;
    overflow: hidden;
    background: var(--backdrop);
    font-family: "Poppins", sans-serif;
  }
  .canvas { position: relative; width: 1189px; height: 1200px; }
  .card {
    position: absolute;
    left: 184px;
    width: 820px;
    height: 536px;
    box-shadow: 0 6px 18px var(--shadow);
  }
  .card--front { top: 40px; background: var(--card-white); }
  .card--back  { top: 623px; background: var(--brand-blue); }

  .wordmark {
    color: var(--card-white);
    font-weight: 600;
    line-height: 1.3;
    white-space: nowrap;
  }
  .tagline {
    color: var(--card-white);
    font-weight: 600;
    white-space: nowrap;
    line-height: 1;
  }

  .logo-band {
    position: absolute;
    left: 0;
    top: 196px;
    width: 481px;
    height: 112px;
    background: var(--brand-blue);
  }
  .logo-band .wordmark {
    position: absolute;
    left: 43px;
    top: 0;
    font-size: 58px;
    letter-spacing: -0.5px;
  }
  .logo-band .tagline {
    position: absolute;
    left: 45px;
    top: 83px;
    font-size: 15px;
    letter-spacing: 2.4px;
  }

  .contact { position: absolute; top: 340px; color: var(--brand-blue); }
  .contact--callum { left: 43px; }
  .contact--marcus { left: 356px; }
  .contact__name {
    font-weight: 600;
    font-size: 24px;
    line-height: 30px;
    letter-spacing: 0.6px;
    text-transform: uppercase;
  }
  .contact__role {
    font-size: 19px;
    line-height: 24px;
    letter-spacing: 0.8px;
  }
  .contact__list { list-style: none; margin-top: 16px; }
  .contact__item {
    display: flex;
    align-items: center;
    font-size: 20px;
    line-height: 28px;
    letter-spacing: 0.5px;
    white-space: nowrap;
  }
  .contact__icon {
    width: 20px;
    height: 16px;
    margin-right: 12px;
    flex: none;
    fill: var(--brand-blue);
  }
  .contact__icon--web { fill: none; stroke: var(--brand-blue); stroke-width: 1.5; }
  .divider {
    position: absolute;
    left: 335px;
    top: 342px;
    width: 2px;
    height: 150px;
    background: var(--brand-blue);
  }

  .back-logo {
    position: absolute;
    left: 0;
    right: 0;
    top: 190px;
    display: flex;
    flex-direction: column;
    align-items: center;
  }
  .back-logo .wordmark { font-size: 80px; letter-spacing: -1px; }
  .back-logo .tagline { margin-top: 4px; font-size: 22px; letter-spacing: 3.4px; }
</style>
</head>
<body>
<main class="canvas">
  <section class="card card--front" aria-label="Business card front">
    <div class="logo-band">
      <div class="wordmark">FairlyNeat</div>
      <div class="tagline">Shaping Causes With Heart</div>
    </div>

    <div class="contact contact--callum">
      <div class="contact__name">Callum Ferris</div>
      <div class="contact__role">Founder &amp; CEO</div>
      <ul class="contact__list">
        <li class="contact__item">
          <svg class="contact__icon" viewBox="0 0 20 16" aria-hidden="true"><path d="M5 1c1-.6 2-.4 2.4.4l1 2.2c.3.7 0 1.3-.6 1.6l-.8.4c.2 2 1 3.8 2.3 5.3l.8-.3c.6-.3 1.3-.1 1.6.5l1.2 2c.4.7.1 1.5-.6 1.9-1 .5-2.3.6-3.4-.2C6.6 11.7 5 8 4.6 3.6 4.5 2.6 4.6 1.5 5 1z"/></svg>
          021 684 2590
        </li>
        <li class="contact__item">
          <svg class="contact__icon" viewBox="0 0 20 16" aria-hidden="true"><path d="M0 2h20v12H0z M2 3.5l8 6 8-6v-.1H2z" fill-rule="evenodd"/></svg>
          hello@fairlyneat.nz
        </li>
        <li class="contact__item">
          <svg class="contact__icon contact__icon--web" viewBox="0 0 20 16" aria-hidden="true"><circle cx="10" cy="8" r="6.5"/><ellipse cx="10" cy="8" rx="2.8" ry="6.5"/><path d="M3.5 8h13"/></svg>
          www.fairlyneat.nz
        </li>
      </ul>
    </div>

    <div class="divider"></div>

    <div class="contact contact--marcus">
      <div class="contact__name">Marcus Delaney</div>
      <div class="contact__role">Co-Founder &amp; Chief Product Officer</div>
      <ul class="contact__list">
        <li class="contact__item">
          <svg class="contact__icon" viewBox="0 0 20 16" aria-hidden="true"><path d="M5 1c1-.6 2-.4 2.4.4l1 2.2c.3.7 0 1.3-.6 1.6l-.8.4c.2 2 1 3.8 2.3 5.3l.8-.3c.6-.3 1.3-.1 1.6.5l1.2 2c.4.7.1 1.5-.6 1.9-1 .5-2.3.6-3.4-.2C6.6 11.7 5 8 4.6 3.6 4.5 2.6 4.6 1.5 5 1z"/></svg>
          0279831465
        </li>
        <li class="contact__item">
          <svg class="contact__icon" viewBox="0 0 20 16" aria-hidden="true"><path d="M0 2h20v12H0z M2 3.5l8 6 8-6v-.1H2z" fill-rule="evenodd"/></svg>
          marcus@fairlyneat.nz
        </li>
        <li class="contact__item">
          <svg class="contact__icon contact__icon--web" viewBox="0 0 20 16" aria-hidden="true"><circle cx="10" cy="8" r="6.5"/><ellipse cx="10" cy="8" rx="2.8" ry="6.5"/><path d="M3.5 8h13"/></svg>
          www.fairlyneat.nz
        </li>
      </ul>
    </div>
  </section>

  <section class="card card--back" aria-label="Business card back">
    <div class="back-logo">
      <div class="wordmark">FairlyNeat</div>
      <div class="tagline">Shaping Causes With Heart</div>
    </div>
  </section>
</main>
</body>
</html>
```